Velmora and Co Business Card Design

Looking for a business card design. Wanting Smart, Clean and Sharp looking to promote Velmora and Co, our Import Export Business - like Black, White and natural textures. I have uploaded our logo. I like a rounded font but open to other ideas
Being that we have a wide range of products on offer we are looking for a neutral yet eye catching card. We would also like to have Import - Export on the business card to be clear on want our business does.

Target Market(s)

Import export market

Industry/Entity Type

Importer

Contact Information for Business Card

Mr Tobias Kernwell
tobias.kernwell@velmoraandco.com.au
+61 (0) 417 630 284
www.velmoraandco.com.au

Font styles to use
Other font styles liked:
• Unsure of actual font name but something rounded and clean

Colors

Designer to choose colors to be used in the design.

Requirements
Must have
• Instagram icon
• Facebook icon

```html
<!DOCTYPE html>
<html lang="en">
<head>
<meta charset="utf-8">
<title>Velmora and Co Business Card</title>
<link rel="stylesheet" href="https://fonts.googleapis.com/css2?family=Nunito:wght@400;600;700&display=swap">
<style>
  :root {
    --backdrop: #f3f3f3;
    --ink: #231f20;
    --paper: #ffffff;
    --shadow: rgba(0, 0, 0, 0.28);
  }
  * { margin: 0; padding: 0; box-sizing: border-box; }
  html, body { width: 1200px; height: 900px; overflow: hidden; }
  body {
    background: var(--backdrop);
    font-family: "Nunito", sans-serif;
    position: relative;
  }
  .card {
    position: absolute;
    border-radius: 22px;
    overflow: hidden;
    box-shadow: 0 6px 14px var(--shadow);
  }
  .card-front {
    left: 290px; top: 76px; width: 620px; height: 354px;
    background: var(--ink);
    color: var(--paper);
  }
  .front-brand {
    position: absolute; left: 0; right: 0; top: 152px;
    text-align: center;
    font-size: 40px; font-weight: 700; letter-spacing: 1px;
    line-height: 1;
  }
  .front-tagline {
    position: absolute; left: 0; right: 0; top: 269px;
    text-align: center;
    font-size: 17px; font-weight: 400; letter-spacing: 2.4px;
  }
  .card-back {
    left: 287px; top: 468px; width: 624px; height: 356px;
    background: var(--paper);
    color: var(--ink);
  }
  .back-brand {
    position: absolute; left: 70px; top: 134px; width: 160px;
    text-align: center;
    font-size: 24px; font-weight: 700; line-height: 1.15;
    color: var(--ink);
  }
  .contact-block { position: absolute; left: 276px; top: 94px; }
  .person-name { font-size: 19px; font-weight: 400; line-height: 1.2; }
  .person-name strong { font-weight: 700; }
  .person-role { font-size: 14.5px; margin-top: 2px; }
  .contact-list { list-style: none; margin-top: 14px; }
  .contact-list li {
    display: flex; align-items: center;
    font-size: 16px; height: 27.5px;
  }
  .contact-list svg { width: 19px; height: 19px; margin-right: 9px; fill: var(--ink); }
  .wave { position: absolute; left: 0; top: 0; }
  .social {
    position: absolute; right: 46px; top: 314px;
    display: flex; align-items: center; gap: 10px;
    color: var(--paper); font-size: 16.5px;
  }
  .social-mark {
    width: 18px; height: 18px; border-radius: 3px;
    background: var(--paper);
  }
</style>
</head>
<body>
  <section class="card card-front">
    <p class="front-brand">VELMORA AND CO</p>
    <p class="front-tagline">IMPORT &amp; EXPORT</p>
  </section>

  <section class="card card-back">
    <svg class="wave" width="624" height="356" viewBox="0 0 624 356" aria-hidden="true">
      <path d="M0,282 C70,302 180,306 285,299 C180,314 70,320 0,316 Z" fill="var(--ink)"/>
      <path d="M0,334 C150,324 300,292 450,280 C530,274 590,286 624,310 L624,356 L0,356 Z" fill="var(--ink)"/>
    </svg>

    <p class="back-brand">Velmora<br>and Co</p>

    <div class="contact-block">
      <p class="person-name">Mr TOBIAS <strong>KERNWELL</strong></p>
      <p class="person-role">CEO | Founder</p>
      <ul class="contact-list">
        <li>
          <svg viewBox="0 0 24 24" aria-hidden="true"><path d="M6.6 10.8a15.1 15.1 0 0 0 6.6 6.6l2.2-2.2a1 1 0 0 1 1-.25 11.4 11.4 0 0 0 3.6.57 1 1 0 0 1 1 1V20a1 1 0 0 1-1 1A17 17 0 0 1 3 4a1 1 0 0 1 1-1h3.5a1 1 0 0 1 1 1c0 1.25.2 2.450.57 3.57a1 1 0 0 1-.25 1z"/></svg>
          +61 (0) 417 630 284
        </li>
        <li>
          <svg viewBox="0 0 24 24" aria-hidden="true"><path d="M3 5h18a1 1 0 0 1 1 1v12a1 1 0 0 1-1 1H3a1 1 0 0 1-1-1V6a1 1 0 0 1 1-1zm9 7.2L20 8V7l-8 4.2L4 7v1z"/></svg>
          tobias.kernwell@velmoraandco.com.au
        </li>
        <li>
          <svg viewBox="0 0 24 24" aria-hidden="true"><circle cx="12" cy="12" r="9.5" fill="none" stroke="var(--ink)" stroke-width="2"/><path d="M7 6c2 1 1 3 3 3s1 3 3 3-1 3-3 4l-1 3c-3-1-5-4-5-7 0-2 1-4 3-6zm9 1c1 1 3 3 2 6-1 0-2-1-2-2s-2-1-2-2 1-2 2-2z"/></svg>
          www.velmoraandco.com.au
        </li>
      </ul>
    </div>

    <div class="social">
      <span>Follow Us -</span>
      <span class="social-mark" role="img" aria-label="Social profile"></span>
      <span class="social-mark" role="img" aria-label="Photo profile"></span>
    </div>
  </section>
</body>
</html>
```